Business card and company logo design needed

Need a business card and company logo design for all stationary for an Aviation refueling consultancy business. Our business offers consulting services in the specialist aviation refueling industry. Services range from engineering, compliance and management consultancy through to project management services. This encompasses infrastructure from refinery through to airport and into the aircraft wing.

Design should be simple, 'less-is-more' concept, possibly taking advantage of the 'm' for tovel and the fact is it the aviation industry. It should convey confidence, safety, experience, professionalism, aviation, engineering?, and should not be afraid to be simple in color...though please do not let this restrict your designs and imagination.

Target Market(s)

Airport authorities, oil majors, aircraft operators

Industry/Entity Type

Airport

Contact Information for Business Card

Verlin Skyward Advisory Pty Ltd
Dario Tovel
Director
mobile:+61428537104
email: dario@tovelexample.com
Skype: dario.tovelexample

Logo styles of interest
Emblem Logo
Pictorial/Combination Logo
Abstract Logo
Wordmark Logo
Lettermark Logo
Requirements
Must have
• - A feel of safety, security and confidence
Nice to have
• - Aviation has both heritage and modern 'sexy' elements so would be nice to try and capture both
- Aviation 'JET' fuel color is designated as black in signage or labels
- Themes? : Aviation fuel is derived from oil, it burns, safety, Jet fuel is colorless
- Company is global in reach, borderless like aircraft
Should not have
• - Cliche:

```html
<!DOCTYPE html>
<html lang="en">
<head>
<meta charset="utf-8">
<title>Verlin Skyward Advisory Pty Ltd – Business Card</title>
<link rel="stylesheet" href="https://fonts.googleapis.com/css2?family=Bodoni+Moda:opsz,wght@6..96,400&display=swap">
<style>
  :root {
    --panel-grey: #d4d5d7;
    --card-white: #ffffff;
    --base-strip: #f3f3f3;
    --ink: #141414;
    --mark-grey: #5a5a5a;
  }
  * { margin: 0; padding: 0; box-sizing: border-box; }
  html, body {
    width: 1200px;
    height: 693px;
    overflow: hidden;
    background: var(--card-white);
  }
  .card {
    position: relative;
    width: 1200px;
    height: 693px;
    background: var(--card-white);
    font-family: "Bodoni Moda", "Didot", "Times New Roman", serif;
    color: var(--ink);
    overflow: hidden;
  }
  .brand-panel {
    position: absolute;
    left: 0;
    top: 0;
    width: 380px;
    height: 693px;
    background: var(--panel-grey);
  }
  .base-strip {
    position: absolute;
    left: 380px;
    right: 0;
    bottom: 0;
    height: 16px;
    background: var(--base-strip);
  }
  .brand-square {
    position: absolute;
    left: 60px;
    top: 200px;
    width: 260px;
    height: 260px;
    background: var(--mark-grey);
  }
  .company-name {
    position: absolute;
    left: 0;
    top: 496px;
    width: 380px;
    text-align: center;
    font-size: 44px;
    font-weight: 400;
    line-height: 52px;
    color: var(--ink);
  }
  .company-name span { display: block; }
  .person {
    position: absolute;
    right: 30px;
    top: 306px;
    text-align: right;
  }
  .person-name {
    font-size: 64px;
    font-weight: 400;
    line-height: 72px;
  }
  .person-role {
    font-size: 40px;
    font-weight: 400;
    line-height: 52px;
  }
  .contact {
    position: absolute;
    right: 30px;
    top: 512px;
    text-align: right;
    list-style: none;
    font-size: 38px;
    font-weight: 400;
    line-height: 53px;
    white-space: nowrap;
  }
</style>
</head>
<body>
  <div class="card">
    <div class="brand-panel"></div>
    <div class="base-strip"></div>

    <div class="brand-square"></div>
    <p class="company-name">
      <span>Verlin Skyward</span>
      <span>Advisory</span>
      <span>Pty Ltd</span>
    </p>

    <div class="person">
      <p class="person-name">Dario Tovel</p>
      <p class="person-role">Director</p>
    </div>

    <ul class="contact">
      <li>Mobile:+61428537104</li>
      <li>Email: dario@tovelexample.com</li>
      <li>Skype: dario.tovelexample</li>
    </ul>
  </div>
</body>
</html>
```